specialised legal consultancy business needs an update on logo and office stationary.

Update on Logo - see attached.

update on email signature - something new and fresh with only the following details -

(the logo)
Advocate Peter Sandovik
PS Entity Frameworks (Pty) Ltd (Reg No.: 2019 / 153927 / 07)
LLB, LLM (Cum Laude), Cert.Dir (KWBFE), FCG (TREPX)
+27 71 592 6604
peter#kwellbrandt.com

Update on letterhead - something new and fresh and please more user-friendly. With the same details as per the email signature.

```html
<!DOCTYPE html>
<html lang="en">
<head>
<meta charset="utf-8">
<title>Email Signature – Mockup 1</title>
<link href="https://fonts.googleapis.com/css2?family=Poppins:wght@300;600;700&family=Barlow+Semi+Condensed:wght@400&display=swap" rel="stylesheet">
<style>
  :root {
    --ink: #000000;
    --text: #1a1a1a;
    --muted: #7a7a7a;
    --rule: #222222;
    --paper: #ffffff;
    --shadow: rgba(0, 0, 0, 0.22);
  }
  html, body {
    margin: 0;
    padding: 0;
    width: 1200px;
    height: 1200px;
    overflow: hidden;
    background: var(--paper);
  }
  .canvas {
    position: relative;
    width: 1200px;
    height: 1200px;
    font-family: "Poppins", sans-serif;
    color: var(--text);
  }
  .sheet-title {
    position: absolute;
    top: 258px;
    left: 0;
    width: 100%;
    text-align: center;
    font-weight: 600;
    font-size: 24px;
    color: var(--ink);
    margin: 0;
    line-height: 1.2;
  }
  .sheet-subtitle {
    position: absolute;
    top: 293px;
    left: 0;
    width: 100%;
    text-align: center;
    font-weight: 300;
    font-size: 17px;
    color: var(--muted);
    margin: 0;
    line-height: 1.2;
  }
  .signature {
    position: absolute;
    left: 49px;
    top: 438px;
    width: 1076px;
    height: 249px;
    background: var(--paper);
    box-shadow: 0 4px 22px var(--shadow);
  }
  .signature__bar {
    position: absolute;
    top: 0;
    bottom: 0;
    background: var(--ink);
  }
  .signature__bar--thick { left: 0; width: 13px; }
  .signature__bar--thin { left: 16px; width: 4px; }
  .signature__name {
    position: absolute;
    left: 50px;
    top: 39px;
    margin: 0;
    font-family: "Poppins", sans-serif;
    font-weight: 700;
    font-size: 27px;
    letter-spacing: 0.8px;
    color: var(--ink);
    line-height: 1.2;
  }
  .signature__rule {
    position: absolute;
    left: 50px;
    width: 513px;
    height: 1px;
    background: var(--rule);
  }
  .signature__rule--top { top: 82px; }
  .signature__rule--bottom { top: 158px; }
  .signature__details,
  .signature__contact {
    position: absolute;
    left: 50px;
    margin: 0;
    font-family: "Barlow Semi Condensed", sans-serif;
    font-size: 17.5px;
    line-height: 25.5px;
    letter-spacing: 0.3px;
    color: var(--text);
  }
  .signature__details { top: 96px; }
  .signature__contact { top: 171px; }
  .signature__brand {
    position: absolute;
    right: 26px;
    top: 186px;
    display: flex;
    align-items: center;
    gap: 10px;
  }
  .signature__brand-mark {
    width: 16px;
    height: 16px;
    background: var(--ink);
  }
  .signature__brand-name {
    font-family: "Poppins", sans-serif;
    font-weight: 700;
    font-size: 21px;
    letter-spacing: 1.6px;
    color: var(--ink);
    line-height: 1;
  }
</style>
</head>
<body>
  <main class="canvas">
    <h1 class="sheet-title">email signature Mockup 1</h1>
    <p class="sheet-subtitle">Size: as per existing Signature</p>

    <section class="signature" aria-label="Email signature">
      <div class="signature__bar signature__bar--thick"></div>
      <div class="signature__bar signature__bar--thin"></div>

      <h2 class="signature__name">Advocate Peter Sandovik</h2>
      <div class="signature__rule signature__rule--top"></div>

      <p class="signature__details">
        PS Entity Frameworks (Pty) Ltd (Reg No.: 2019 / 153927 / 07)<br>
        LLB, LLM (Cum Laude), Cert.Dir (KWBFE), FCG (TREPX)
      </p>
      <div class="signature__rule signature__rule--bottom"></div>

      <p class="signature__contact">
        +27 71 592 6604<br>
        peter@kwellbrandt.com
      </p>

      <div class="signature__brand">
        <span class="signature__brand-mark"></span>
        <span class="signature__brand-name">PS FRAMEWORKS</span>
      </div>
    </section>
  </main>
</body>
</html>
```